Ledger Grove Pilot Banner Ad campaign

We are the number 1 leading automated journal & analytics platform for active traders in the crypto space

We will be running banner ads on a specialist ad network and need HTML designs + a good strategy.

Some of our key selling points to consider including:

- The #1 automated journaling & analytics solution for Crypto Traders
- We save traders time (from manual data entry that can be automated by our journal trade import service)
- We help traders improve through detailed analytics feedback on their trading performance
- LGP has helped thousands of crypto traders improve performance
- 5,700+ traders are using LGP to save themselves hundreds of data entry hours per year
- Analyse your full trade history in a click!

I have attached an example mockup we came up with internally but we are not professionals. Use it as a guide to heavily improve upon in the context of general design quality, and 'sales-y' lingo to improve conversions
Updates

Have added a £100 1st place payment increase upon advice from a designer Should incentivise the best of the best to submit work

Target Market(s)

Active traders in the crypto derivatives space. Trading on the following exchanges:

- Trelvax.example
- Quorvane.example
- Pelmiro.example
- ZQB.example

Font styles to use
Other font styles liked:
• Quicksand is our main font atm

Colors
3277b5
33a6d7
0792cd
85abd2
3276b5
85acd3
85cae6
86cae7

Requirements
Must have
• similar colour scheme from my example upload.

Check our main website for more: ledgergrovepilot.example

Although bare in mind, its a bit old and shitty. We are now working with specialists to improve, so feel free to have some creative freedom
Nice to have
• Nice clear custom icons to accompany text. And a rotation of 2 or 3 of the main selling points from the project description

```html
<!DOCTYPE html>
<html lang="en">
<head>
<meta charset="utf-8">
<title>Ledger Grove Pilot — Banner</title>
<link rel="stylesheet" href="https://fonts.googleapis.com/css2?family=Quicksand:wght@300;400;700&display=swap">
<style>
  :root {
    --bg-top: #52a9b8;
    --bg-mid: #479bbc;
    --bg-bottom: #3a78b2;
    --white: #ffffff;
    --highlight: #f8ea4a;
    --cta-top: #fffcc0;
    --cta-bottom: #fff22e;
    --cta-text: #111111;
    --art-light: #85cae6;
    --art-mid: #33a6d7;
    --art-deep: #3277b5;
    --art-gold: #f1c15a;
  }
  html, body {
    margin: 0;
    padding: 0;
    width: 1200px;
    height: 1004px;
    overflow: hidden;
  }
  .banner {
    position: relative;
    width: 1200px;
    height: 1004px;
    background: linear-gradient(180deg, var(--bg-top) 0%, var(--bg-mid) 50%, var(--bg-bottom) 100%);
    font-family: "Quicksand", sans-serif;
    color: var(--white);
    overflow: hidden;
  }
  .brand {
    position: absolute;
    left: 143px;
    top: 78px;
    display: flex;
    align-items: center;
    gap: 58px;
  }
  .brand-mark {
    width: 92px;
    height: 92px;
    box-sizing: border-box;
    border: 3px solid var(--white);
  }
  .brand-name {
    font-weight: 300;
    font-size: 55px;
    letter-spacing: 3px;
    line-height: 1;
    white-space: nowrap;
  }
  .headline {
    position: absolute;
    left: 147px;
    top: 364px;
    margin: 0;
    font-weight: 300;
    font-size: 41px;
    line-height: 58px;
    letter-spacing: 0.3px;
  }
  .headline .accent {
    font-weight: 700;
    color: var(--highlight);
  }
  .headline .strong {
    font-weight: 700;
  }
  .growth-art {
    position: absolute;
    left: 695px;
    top: 225px;
    width: 375px;
    height: 520px;
    border-radius: 18px;
    background:
      radial-gradient(circle at 78% 82%, rgba(241, 193, 90, 0.55) 0%, rgba(241, 193, 90, 0) 38%),
      linear-gradient(200deg, var(--art-light) 0%, var(--art-mid) 55%, var(--art-deep) 100%);
    opacity: 0.75;
  }
  .cta {
    position: absolute;
    left: 235px;
    top: 785px;
    width: 730px;
    height: 137px;
    border-radius: 69px;
    background: linear-gradient(180deg, var(--cta-top) 0%, var(--cta-bottom) 100%);
    box-shadow: 0 6px 18px rgba(20, 60, 110, 0.25);
    display: flex;
    align-items: center;
    justify-content: center;
    color: var(--cta-text);
    font-weight: 700;
    font-size: 38px;
    letter-spacing: 0.5px;
    text-decoration: none;
  }
</style>
</head>
<body>
  <div class="banner">
    <header class="brand">
      <span class="brand-mark" aria-hidden="true"></span>
      <span class="brand-name">LEDGER GROVE PILOT</span>
    </header>

    <h1 class="headline">
      LGP has helped <span class="accent">thousands</span><br>
      of crypto traders <span class="strong">improve</span><br>
      <span class="strong">performance</span>
    </h1>

    <div class="growth-art" role="img" aria-label="Illustration of rising blue 3D bar chart with stacks of gold coins"></div>

    <a class="cta" href="#">START YOUR FREE TRIAL NOW</a>
  </div>
</body>
</html>
```